New Zealand Marlborough Sauvignon Blanc wine packaging design

We need packaging design for our new wine brand, Dunmore Hale. The wine is a New Zealand Marlborough Sauvignon Blanc. We would like the packaging will portray elegance and style with an understated label. We are looking for a label that portrays the elegance of the French Riviera. The label should be round or pill shaped.
Updates

Industry/Entity Type

Wine

Font styles to use
Serif
Sans Serif

Requirements
Must have
• The words in order of importance: Dunmore Hale, Sauvignon Blanc, Marlborough, New Zealand. It should be fit to the bottle posted in the links
Nice to have
• a pill shape or circular shape
Should not have
• Illustrations of wine bottles, wine glasses, or grapes

```html
<!DOCTYPE html>
<html lang="en">
<head>
<meta charset="utf-8">
<title>Dunmore Hale – Sauvignon Blanc Label</title>
<link rel="stylesheet" href="https://fonts.googleapis.com/css2?family=Baloo+2:wght@600;700&family=Source+Sans+3:wght@400&display=swap">
<style>
  :root {
    --ink: #231f20;
    --paper: #ffffff;
    --art-light: #f1f0ee;
    --art-mid: #dcdad6;
  }
  html, body {
    margin: 0;
    padding: 0;
    width: 1200px;
    height: 1000px;
    overflow: hidden;
    background: var(--paper);
  }
  .sheet { display: block; width: 1200px; height: 1000px; }
  .dimension-line { stroke: var(--ink); stroke-width: 1; fill: none; }
  .dimension-label {
    font-family: "Source Sans 3", sans-serif;
    font-size: 20px;
    fill: var(--ink);
  }
  .label-outline { fill: var(--paper); stroke: var(--ink); stroke-width: 1.4; }
  .label-ring { fill: none; stroke: var(--ink); stroke-width: 5; }
  .window-frame { fill: none; stroke: var(--ink); stroke-width: 9; }
  .window-inner-line { fill: none; stroke: var(--ink); stroke-width: 1.4; }
  .arc-text {
    font-family: "Baloo 2", sans-serif;
    font-weight: 700;
    font-size: 32px;
    letter-spacing: 11px;
    fill: var(--ink);
  }
  .origin-line {
    font-family: "Baloo 2", sans-serif;
    font-weight: 600;
    font-size: 13px;
    letter-spacing: 2px;
    fill: var(--ink);
  }
  .brand-name {
    font-family: "Baloo 2", sans-serif;
    font-weight: 700;
    font-size: 44px;
    fill: var(--ink);
  }
  .swatch { fill: var(--ink); }
  .swatch-label {
    font-family: "Source Sans 3", sans-serif;
    font-size: 31px;
    fill: var(--ink);
  }
</style>
</head>
<body>
<svg class="sheet" viewBox="0 0 1200 1000" xmlns="http://www.w3.org/2000/svg">
  <defs>
    <marker id="arrowhead" viewBox="0 0 10 10" refX="10" refY="5" markerWidth="9" markerHeight="9" orient="auto-start-reverse">
      <path d="M0 1 L10 5 L0 9" fill="none" stroke="#231f20" stroke-width="1.2"/>
    </marker>
    <linearGradient id="artTone" x1="0" y1="0" x2="0" y2="1">
      <stop offset="0" stop-color="var(--art-light)"/>
      <stop offset="1" stop-color="var(--art-mid)"/>
    </linearGradient>
    <clipPath id="window-clip">
      <rect x="478" y="298" width="268" height="394" rx="131" ry="152"/>
    </clipPath>
    <path id="arc-top" d="M 422 420 A 190 168 0 0 1 802 420"/>
    <path id="arc-bottom" d="M 430 640 A 178 128 0 0 0 786 640"/>
  </defs>

  <g class="dimension width-dimension">
    <line class="dimension-line" x1="359" y1="117" x2="359" y2="205"/>
    <line class="dimension-line" x1="855" y1="117" x2="855" y2="205"/>
    <line class="dimension-line" x1="360" y1="126" x2="854" y2="126" marker-start="url(#arrowhead)" marker-end="url(#arrowhead)"/>
    <text class="dimension-label" x="598" y="110" text-anchor="middle">80mm</text>
  </g>

  <g class="dimension height-dimension">
    <line class="dimension-line" x1="288" y1="180" x2="377" y2="180"/>
    <line class="dimension-line" x1="288" y1="804" x2="377" y2="804"/>
    <line class="dimension-line" x1="291" y1="181" x2="291" y2="803" marker-start="url(#arrowhead)" marker-end="url(#arrowhead)"/>
    <text class="dimension-label" x="264" y="534" text-anchor="middle" transform="rotate(-90 264 534)" dy="7">100mm</text>
  </g>

  <g class="wine-label">
    <rect class="label-outline" x="360" y="195" width="495" height="609" rx="235" ry="262"/>
    <rect class="label-ring" x="396" y="214" width="426" height="560" rx="205" ry="240"/>

    <text class="arc-text varietal"><textPath href="#arc-top" startOffset="50%" text-anchor="middle">SAUVIGNON BLANC</textPath></text>
    <text class="arc-text region"><textPath href="#arc-bottom" startOffset="50%" text-anchor="middle">MARLBOROUGH</textPath></text>

    <rect class="side-ornament" x="409" y="456" width="22" height="110" rx="8" fill="url(#artTone)" role="img" aria-label="Small decorative flourish"/>
    <rect class="side-ornament" x="792" y="456" width="22" height="110" rx="8" fill="url(#artTone)" role="img" aria-label="Small decorative flourish"/>

    <rect class="window-frame" x="459" y="279" width="306" height="432" rx="150" ry="172"/>
    <rect class="window-inner-line" x="470" y="290" width="284" height="410" rx="139" ry="160"/>

    <text class="origin-line" x="612" y="314" text-anchor="middle">NEW ZEALAND</text>

    <g clip-path="url(#window-clip)">
      <rect class="scene-illustration" x="470" y="322" width="284" height="266" fill="url(#artTone)" role="img" aria-label="Line illustration of a dancing woman in a starred gown framed by blossom garlands, mountains and a river behind"/>
    </g>

    <text class="brand-name" x="612" y="633" text-anchor="middle">DUNMORE</text>
    <text class="brand-name" x="612" y="677" text-anchor="middle">HALE</text>
  </g>

  <g class="ink-legend">
    <rect class="swatch" x="440" y="888" width="26" height="33"/>
    <text class="swatch-label" x="492" y="916">BLACK</text>
  </g>
</svg>
</body>
</html>
```